Flyer Re-Design

We need a flyer re-design for a company that recently started doing it's own graphic design. Although we've taken a first attempt at the design, we would like a design professional, like yourself show us how much better you can do it. We're going through a re-branding as the logo reads "formerly" known as and although we'd like to keep the logo as it is---everything else should be more contemporary.

5.5" x 8.5" or 5" x 7"

Target Market(s)

Bahamas Youth

Industry/Entity Type

Graphic Design

Font styles to use
Sans Serif

Requirements
Must have
• Current Logo. Include as many details as already listed in the document.
Nice to have
• Fresh New, Crisp Ideas for this Pharmacy rebranding
Should not have
• Too Many colors or serif fonts

```html
<!DOCTYPE html>
<html lang="en">
<head>
<meta charset="utf-8">
<title>Rewards Club Flyer – Vital Path Pharmacy</title>
<link rel="stylesheet" href="https://fonts.googleapis.com/css2?family=Nunito:ital,wght@0,600;0,800;0,900;1,900&family=Nunito+Sans:wght@400;500;700;800&display=swap">
<style>
  :root {
    --red: #ec1c24;
    --red-deep: #b8121a;
    --cream: #fbf6c6;
    --ink: #151515;
    --white: #ffffff;
    --sky: #cde9fa;
    --brand-green: #2e7d32;
  }
  * { margin: 0; padding: 0; box-sizing: border-box; }
  html, body { width: 857px; height: 1200px; overflow: hidden; background: var(--white); }
  .flyer { position: relative; width: 857px; height: 1200px; font-family: "Nunito Sans", Arial, sans-serif; }
  .flyer__red { position: absolute; left: 0; top: 0; width: 857px; height: 1050px; background: var(--red); }

  .bubble { position: absolute; left: 0; top: 0; }
  .bubble__text { position: absolute; left: 60px; top: 50px; width: 737px; height: 220px; display: flex; flex-direction: column; justify-content: center; align-items: center; color: var(--ink); font-family: "Nunito", sans-serif; }
  .bubble__lead { font-weight: 600; font-size: 36px; line-height: 1.1; }
  .bubble__title { font-weight: 900; font-size: 88px; line-height: 1; letter-spacing: 2px; margin-top: 6px; }

  .club { position: absolute; left: 115px; top: 330px; color: var(--white); }
  .club__heading { font-weight: 800; font-size: 30px; line-height: 40px; white-space: nowrap; }
  .club__rule { width: 64px; height: 5px; border-radius: 3px; background: var(--cream); margin-top: 8px; }
  .club__list { list-style: none; position: absolute; left: 0; font-size: 25px; font-weight: 500; line-height: 40px; white-space: nowrap; }
  .club__list--points { top: 68px; }
  .club__label { position: absolute; left: 0; top: 250px; font-size: 25px; font-weight: 800; line-height: 40px; color: var(--cream); text-transform: uppercase; letter-spacing: 2px; }
  .club__list--exclusives { top: 292px; }
  .club__list li { position: relative; padding-left: 30px; }
  .club__list li::before { content: ""; position: absolute; left: 0; top: 15px; width: 12px; height: 12px; border-radius: 50%; background: var(--cream); }
  .club__list strong { font-weight: 800; }

  .gift { position: absolute; left: 0; top: 850px; }
  .gift__text { position: absolute; left: 110px; top: 850px; height: 96px; display: flex; align-items: center; gap: 16px; font-family: "Nunito", sans-serif; color: var(--ink); white-space: nowrap; }
  .gift__big { font-style: italic; font-weight: 900; font-size: 46px; letter-spacing: 1px; }
  .gift__small { font-weight: 800; font-size: 32px; }

  .cta { position: absolute; left: 0; top: 990px; width: 857px; text-align: center; color: var(--white); font-weight: 800; font-size: 23px; white-space: nowrap; }

  .brand { position: absolute; left: 0; top: 1068px; width: 857px; display: flex; justify-content: center; align-items: center; gap: 12px; }
  .brand__dot { width: 24px; height: 24px; border-radius: 50%; background: var(--brand-green); }
  .brand__name { font-weight: 800; font-size: 26px; color: var(--brand-green); letter-spacing: 0.5px; }
  .web { position: absolute; left: 0; top: 1130px; width: 857px; text-align: center; font-size: 25px; font-weight: 500; color: var(--ink); letter-spacing: 0.3px; }
</style>
</head>
<body>
<main class="flyer">
  <div class="flyer__red"></div>

  <svg class="bubble" width="857" height="330" viewBox="0 0 857 330" aria-hidden="true">
    <rect x="76" y="66" width="737" height="220" rx="44" fill="var(--red-deep)"/>
    <path d="M166 300 L146 326 L246 286 Z" fill="var(--red-deep)"/>
    <rect x="60" y="50" width="737" height="220" rx="44" fill="var(--cream)"/>
    <path d="M150 262 L130 312 L232 268 Z" fill="var(--cream)"/>
  </svg>
  <div class="bubble__text">
    <p class="bubble__lead">It’s just our way of saying</p>
    <h1 class="bubble__title">THANK YOU</h1>
  </div>

  <section class="club">
    <h2 class="club__heading">Join our rewards club</h2>
    <div class="club__rule"></div>
    <ul class="club__list club__list--points">
      <li>Absolutely <strong>Free to Join</strong></li>
      <li>You’ll earn <strong>1 point</strong> for every dollar you spend</li>
      <li>Earn <strong>double points</strong> on selected items purchased</li>
      <li>Earn <strong>25 points</strong> when you refer a friend</li>
    </ul>
    <p class="club__label">Exclusives:</p>
    <ul class="club__list club__list--exclusives">
      <li><strong>VIP access</strong> to our special events</li>
      <li>Be the first to know about our <strong>specials</strong></li>
      <li>Receive notice on <strong>non-advertised specials</strong></li>
      <li><strong>Free subscription</strong> to our online newsletter</li>
      <li>Special “members only” <strong>shopping events</strong></li>
    </ul>
  </section>

  <svg class="gift" width="857" height="96" viewBox="0 0 857 96" aria-hidden="true">
    <path d="M60 8 H857 L805 48 L857 88 H60 Q52 88 52 80 V16 Q52 8 60 8 Z" fill="var(--sky)"/>
  </svg>
  <div class="gift__text"><span class="gift__big">FREE GIFT</span><span class="gift__small">with sign up</span></div>

  <p class="cta">See our customer service representative today!</p>

  <div class="brand">
    <span class="brand__dot"></span>
    <span class="brand__name">Vital Path Pharmacy</span>
  </div>
  <p class="web">www.vitalpathpharmacy.com</p>
</main>
</body>
</html>
```